Business card design for a world class martial arts and group fitness facility

We need a professional and eye catching design for a business card. The card will be used in networking as well as marketing.
We are a martial arts facility offering Taekwondo, Brazilian Jiu Jitsu, and group fitness. All of our programs are geared for kids and adults.
Our Taekwondo program is lead by a Hall of Fame instructor who was Instructor of the Year in 2015.
Our Brazilian Jiu Jitsu program is lead by a wold class instructor who is also a part of the renown Brazilian KLO team.
We offer 3 focused group fitness programs: Ridge kickboxing, Tandem Fitness, and The Quarry which are all lead by certified instructors in a small group setting.
Our facility is state of the art and has been recognized as such in nationally published magazines.
Our business is named The Forge which is the linear logo that is attached. This is the main logo. I also attached a circular logo we have used in some marketing material. Our Jiu Jitsu program is the KLO team logo. The Taekwondo program is the VORTEN Prime. It would be nice to somehow incorporate all 3 logos, but The Forge is most important.
We would like to use all 3 logos if possible but The Forge is the most important. We would like to have a place for a staff member's name while keeping the focus on the programs we offer.

```html
<!DOCTYPE html>
<html lang="en">
<head>
<meta charset="utf-8">
<title>The Forge – Business Card</title>
<link rel="stylesheet" href="https://fonts.googleapis.com/css2?family=Open+Sans:wght@400;800&display=swap">
<style>
  :root {
    --backdrop: #7d7d7d;
    --card: #ffffff;
    --ink: #0a0a0a;
    --wave-grey: #b4b4b4;
    --on-dark: #ffffff;
    --badge-navy: #1f2a5c;
    --badge-red: #d42a2a;
  }
  html, body {
    margin: 0;
    padding: 0;
    width: 992px;
    height: 1200px;
    overflow: hidden;
    background: var(--backdrop);
    font-family: "Open Sans", Arial, sans-serif;
  }
  .card {
    position: absolute;
    left: 68px;
    width: 861px;
    background: var(--card);
    box-shadow: 6px 8px 8px rgba(0,0,0,0.45);
    overflow: hidden;
  }
  .card--front { top: 66px; height: 491px; }
  .card--back  { top: 622px; height: 489px; }

  .wave { position: absolute; inset: 0; width: 100%; height: 100%; }

  .brand {
    position: absolute;
    margin: 0;
    font-weight: 800;
    color: var(--ink);
    letter-spacing: 2px;
    line-height: 1;
    text-transform: uppercase;
    white-space: nowrap;
  }
  .card--front .brand { left: 76px; top: 70px; font-size: 94px; }
  .card--back .brand  { left: 0; right: 0; text-align: center; top: 118px; font-size: 118px; }

  .staff {
    position: absolute;
    right: 46px;
    top: 242px;
    text-align: right;
    color: var(--on-dark);
  }
  .staff__name { margin: 0; font-size: 34px; line-height: 1.1; }
  .staff__role { margin: 4px 0 0; font-size: 22px; }

  .contact {
    position: absolute;
    right: 48px;
    top: 366px;
    margin: 0;
    padding: 0;
    list-style: none;
    color: var(--on-dark);
    font-size: 21px;
  }
  .contact li {
    display: flex;
    justify-content: flex-end;
    align-items: center;
    gap: 26px;
    height: 31.5px;
  }
  .contact svg { width: 17px; height: 17px; flex: none; }

  .address {
    position: absolute;
    left: 38px;
    top: 404px;
    margin: 0;
    font-style: normal;
    color: var(--on-dark);
    font-size: 21px;
    line-height: 31px;
  }

  .program-badge { position: absolute; }
  .program-badge--square {
    left: 238px; top: 333px; width: 134px; height: 111px;
    background: var(--badge-navy);
    border-top: 6px solid var(--badge-red);
    box-sizing: border-box;
  }
  .program-badge--round {
    left: 481px; top: 320px; width: 122px; height: 122px;
    border-radius: 50%;
    background: var(--ink);
    border: 3px solid var(--badge-red);
    box-sizing: border-box;
  }
</style>
</head>
<body>

<section class="card card--front">
  <svg class="wave" viewBox="0 0 861 491" preserveAspectRatio="none" aria-hidden="true">
    <path fill="var(--wave-grey)" d="M0,188 C90,318 240,362 338,343 C500,312 600,128 861,78 L861,491 L0,491 Z"/>
    <path fill="var(--ink)" d="M0,198 C90,330 240,378 338,360 C500,330 600,150 861,96 L861,491 L0,491 Z"/>
  </svg>

  <h1 class="brand">The Forge</h1>

  <div class="staff">
    <p class="staff__name">Dana Whitlock</p>
    <p class="staff__role">Personal Trainer</p>
  </div>

  <ul class="contact">
    <li>0412555019
      <svg viewBox="0 0 17 17"><rect width="17" height="17" rx="2" fill="#fff"/><path d="M5 3.5 L7 3.5 L7.6 6.3 L6.4 7.3 C7.1 8.8 8.2 9.9 9.7 10.6 L10.7 9.4 L13.5 10 L13.5 12 C13.5 12.8 12.8 13.5 12 13.5 C7.6 13.2 3.8 9.4 3.5 5 C3.5 4.2 4.2 3.5 5 3.5 Z" fill="#0a0a0a"/></svg>
    </li>
    <li>dwhitlock@mailbox.com
      <svg viewBox="0 0 17 17"><rect width="17" height="17" rx="2" fill="#fff"/><rect x="3" y="5" width="11" height="7.5" fill="none" stroke="#0a0a0a" stroke-width="1.2"/><path d="M3 5 L8.5 9.3 L14 5" fill="none" stroke="#0a0a0a" stroke-width="1.2"/></svg>
    </li>
    <li>www.forgestudio.com
      <svg viewBox="0 0 17 17"><rect width="17" height="17" rx="2" fill="#fff"/><circle cx="8.5" cy="8.5" r="5.2" fill="none" stroke="#0a0a0a" stroke-width="1.2"/><path d="M3.3 8.5 H13.7 M8.5 3.3 C6.5 6 6.5 11 8.5 13.7 M8.5 3.3 C10.5 6 10.5 11 8.5 13.7" fill="none" stroke="#0a0a0a" stroke-width="1"/></svg>
    </li>
  </ul>

  <address class="address">
    Yarrowbank QLD 4870<br>
    18 Kestrel Drive
  </address>
</section>

<section class="card card--back">
  <h2 class="brand">The Forge</h2>
  <div class="program-badge program-badge--square" role="img" aria-label="VORTEN Prime taekwondo program badge"></div>
  <div class="program-badge program-badge--round" role="img" aria-label="KLO jiu jitsu team badge"></div>
</section>

</body>
</html>
```